Veterinary Entrepreneurship Podcast Needs Image Design

I need some images designed for a new podcast called "Veterinary Entrepreneurship: The Morwen Tabrizi Diaries".

I need a cover image for Quill Audiocasts: "Artwork must be in the JPEG or PNG file formats and in the RGB color space with a minimum size of 1400 x 1400 pixels and a maximum size of 3000 x 3000 pixels at 72 DPI."

The podcasts is essentially about me charting daily my journey as an entrepreneur. Looking for a design which is stylish but fun, communicates innovation, dynamism etc. To include the attached head shot photo and one version of the attached signatures.

Target Market(s)

Veterinary

Industry/Entity Type

Veterinary

Font styles to use
Sans Serif

Colors

Designer to choose colors to be used in the design.

Requirements
Must have
• The name of the podcast, my head shot photo and one of the signature files I uploaded.
Nice to have
• Nothing particularly comes to mind
Should not have
• No photos of animals please although happy to see illustrations, outlines etc.

```html
<!DOCTYPE html>
<html lang="en">
<head>
<meta charset="utf-8">
<title>Veterinary Entrepreneurship: The Morwen Tabrizi Diaries</title>
<link rel="stylesheet" href="https://fonts.googleapis.com/css2?family=Roboto+Mono:wght@700&family=Roboto:wght@400&family=Patrick+Hand+SC&display=swap">
<style>
  :root {
    --paper: #ffffff;
    --ink: #0d0d0d;
    --ink-soft: #222222;
    --name-grey: #4f4f4f;
    --burgundy: #7d0f1f;
    --mint: #8ff5e4;
    --night: #050505;
    --amber: #8a4200;
    --skin-light: #e8b597;
    --skin-dark: #a8735a;
    --shirt: #1c1c1e;
  }
  html, body {
    margin: 0;
    padding: 0;
    overflow: hidden;
    background: var(--paper);
  }
  .cover {
    position: relative;
    width: 1200px;
    height: 1200px;
    overflow: hidden;
    background: var(--paper);
  }
  .cover-art {
    position: absolute;
    inset: 0;
  }
  .series-title {
    position: absolute;
    left: 32px;
    top: 22px;
    margin: 0;
    font-family: "Roboto Mono", monospace;
    font-weight: 700;
    font-size: 86px;
    line-height: 104px;
    letter-spacing: -1px;
    color: var(--ink);
  }
  .show-title {
    position: absolute;
    left: 26px;
    top: 246px;
    margin: 0;
    font-weight: 400;
  }
  .show-title .article {
    display: block;
    font-family: "Roboto", sans-serif;
    font-size: 150px;
    line-height: 140px;
    color: var(--ink-soft);
  }
  .show-title .host {
    display: block;
    margin-top: 12px;
    font-family: "Patrick Hand SC", sans-serif;
    font-size: 140px;
    line-height: 144px;
    letter-spacing: 4px;
    color: var(--name-grey);
  }
</style>
</head>
<body>
  <main class="cover">
    <svg class="cover-art" width="1200" height="1200" viewBox="0 0 1200 1200" xmlns="http://www.w3.org/2000/svg">
      <defs>
        <linearGradient id="portrait-tone" x1="0" y1="0" x2="0" y2="1">
          <stop offset="0" stop-color="var(--skin-light)"/>
          <stop offset="0.5" stop-color="var(--skin-dark)"/>
          <stop offset="0.62" stop-color="var(--shirt)"/>
          <stop offset="1" stop-color="var(--shirt)"/>
        </linearGradient>
      </defs>

      <rect class="doodle-panel" x="926" y="0" width="274" height="684" fill="var(--burgundy)"
            role="img" aria-label="Sketched business doodles: handshake, arrows, phone, pie chart, light bulb, document and bar chart"/>

      <path class="host-portrait" role="img" aria-label="Head-shot photo of the host in a dark shirt, smiling"
            fill="url(#portrait-tone)"
            d="M640 300 C700 240 860 230 930 300 C985 350 1000 430 990 520 C985 590 960 640 930 660
               L1060 720 L1200 700 L1200 1200 L536 1200 L540 980 C560 880 620 800 700 760
               C660 720 630 660 620 590 C605 500 600 380 640 300 Z"/>

      <rect class="host-signature" role="img" aria-label="Host's handwritten signature"
            x="184" y="900" width="320" height="80" rx="30" fill="var(--ink)" opacity="0.85"/>

      <g class="corner-shards">
        <polygon points="380,1062 690,1000 600,1200 380,1200" fill="var(--night)"/>
        <polygon points="0,940 900,1200 0,1200" fill="var(--mint)" opacity="0.55"/>
        <polygon points="1200,860 560,1115 560,1200 1200,1200" fill="var(--amber)" opacity="0.82"/>
      </g>
    </svg>

    <h1 class="series-title">VETERINARY<br>ENTREPRENEURSHIP</h1>
    <p class="show-title">
      <span class="article">THE</span>
      <span class="host">MORWEN<br>TABRIZI<br>DIARIES</span>
    </p>
  </main>
</body>
</html>
```